Tranquil Harbour Hypnotherapy 2017 DL Card Flyer

We would like a double sided DL Card Flyer design.

We are a professional Hypnotherapy Clinic looking for a fresh clean design.

Front of card is summary info and back of flyer is detailed text.

I have attached documents with text for the front (dl size hypno 1) and back (dl size hypno 2) of the card and an indicative style of layout.

There are logo files uploaded as well as one image file.

The colors we like are blue, white and yellow/gold.
Updates

please note: when using the 'new mindset new results' image, please only use the top half of the image. The girl is not to be in the image, just the words and light bulb with the chalk underline. thanks.. Added Sunday, March 19, 2017

Industry/Entity Type

Health And Wellness

Requirements
Must have
• Note. I have misspelled the www.TranquilHarbourHypnotherapy.com.au (missing an 'o' in the attachments to the brief). My error. Please amend in your design submissions.

```html
<!DOCTYPE html>
<html lang="en">
<head>
<meta charset="utf-8">
<title>Tranquil Harbour Hypnotherapy – DL Flyer</title>
<link href="https://fonts.googleapis.com/css2?family=Roboto:wght@300;400;500;700&display=swap" rel="stylesheet">
<style>
  :root {
    --navy: #1f2a63;
    --band-blue: #233d8e;
    --gold: #cdb95a;
    --cream: #ece2bd;
    --cream-light: #f8f3e2;
    --white: #ffffff;
    --ink: #2a2a2a;
    --grey: #5f6166;
    --board: #3a3c3e;
  }
  html, body {
    margin: 0;
    padding: 0;
    width: 1200px;
    height: 2400px;
    overflow: hidden;
    background: var(--white);
    font-family: "Roboto", Arial, sans-serif;
  }
  .flyer {
    position: relative;
    width: 1200px;
    height: 2400px;
    overflow: hidden;
    background: var(--white);
  }

  /* Header brand */
  .brand {
    position: absolute;
    top: 112px;
    left: 173px;
    height: 277px;
    display: flex;
    align-items: center;
  }
  .brand-mark {
    width: 277px;
    height: 277px;
    border-radius: 50%;
    background: var(--navy);
    flex: none;
  }
  .brand-divider {
    width: 3px;
    height: 252px;
    background: var(--grey);
    margin: 0 32px 0 28px;
  }
  .brand-name {
    margin: 0;
    font-weight: 700;
    font-size: 56px;
    line-height: 1.1;
    color: var(--navy);
    text-transform: uppercase;
    letter-spacing: 1px;
    white-space: nowrap;
  }

  /* Cream backdrop with curved top */
  .backdrop {
    position: absolute;
    left: 0;
    top: 464px;
    width: 1200px;
    height: 1652px;
    border-top-left-radius: 260px 90px;
    background: linear-gradient(90deg, var(--cream) 0%, var(--cream-light) 55%, var(--cream) 100%);
  }

  /* Quote panel */
  .quote-panel {
    position: absolute;
    left: 83px;
    top: 520px;
    width: 1032px;
    height: 536px;
    box-sizing: border-box;
    background: var(--gold);
    border: 5px solid var(--white);
    border-radius: 150px 0 150px 0;
  }
  .quote-text {
    position: absolute;
    left: 0;
    top: 112px;
    width: 100%;
    margin: 0;
    text-align: center;
    font-weight: 300;
    font-size: 100px;
    line-height: 116px;
    color: var(--white);
  }
  .quote-mark {
    position: absolute;
    font-weight: 700;
    font-size: 300px;
    line-height: 1;
    color: var(--white);
  }
  .quote-mark--open { left: 70px; top: -20px; }
  .quote-mark--close { right: 40px; top: 390px; }

  /* Mindset visual */
  .mindset-visual {
    position: absolute;
    left: 80px;
    top: 1096px;
    width: 1040px;
    height: 389px;
    border-radius: 0 90px 0 110px;
    background: radial-gradient(ellipse at 50% 40%, #5a5850 0%, var(--board) 40%, #2b2d2f 100%);
  }

  /* Programs panel */
  .programs {
    position: absolute;
    left: 83px;
    top: 1528px;
    width: 1032px;
    height: 528px;
    box-sizing: border-box;
    background: var(--gold);
    border: 5px solid var(--white);
    border-radius: 150px 0 150px 0;
  }
  .programs-title {
    position: absolute;
    left: 0;
    top: 61px;
    width: 100%;
    margin: 0;
    text-align: center;
    font-weight: 500;
    font-size: 60px;
    line-height: 66px;
    color: var(--white);
    text-transform: uppercase;
  }
  .programs-list {
    position: absolute;
    top: 0;
    margin: 0;
    padding: 0;
    list-style: none;
    font-size: 35px;
    line-height: 43px;
    color: var(--ink);
  }
  .programs-list li {
    position: absolute;
    left: 0;
    padding-left: 29px;
    white-space: nowrap;
  }
  .programs-list li::before {
    content: "•";
    position: absolute;
    left: 0;
    top: -3px;
    font-size: 26px;
  }
  .programs-list--left { left: 59px; }
  .programs-list--right { left: 514px; }
  .programs-list--right li::before { top: -8px; }

  /* Contact band */
  .contact-band {
    position: absolute;
    left: 0;
    top: 2116px;
    width: 1200px;
    height: 284px;
    background: var(--band-blue);
    color: var(--white);
  }
  .contact-phone {
    position: absolute;
    left: 202px;
    top: 50px;
    display: flex;
    align-items: center;
    gap: 30px;
    font-weight: 400;
    font-size: 108px;
    line-height: 1;
  }
  .phone-icon { width: 104px; height: 104px; flex: none; }
  .contact-web {
    position: absolute;
    left: 0;
    top: 174px;
    width: 100%;
    text-align: center;
    font-size: 32px;
    color: var(--white);
  }
</style>
</head>
<body>
<div class="flyer">

  <header class="brand">
    <div class="brand-mark"></div>
    <div class="brand-divider"></div>
    <p class="brand-name">Tranquil Harbour<br>Hypnotherapy</p>
  </header>

  <div class="backdrop"></div>

  <section class="quote-panel">
    <span class="quote-mark quote-mark--open">“</span>
    <p class="quote-text">There is nothing<br>more important than<br>good health</p>
    <span class="quote-mark quote-mark--close">”</span>
  </section>

  <div class="mindset-visual" role="img" aria-label="Chalkboard with the words New Mindset and New Results around a glowing light bulb"></div>

  <section class="programs">
    <h2 class="programs-title">Professional Hypnosis<br>Therapy Programs:</h2>
    <ul class="programs-list programs-list--left">
      <li style="top:225px">Weight Loss (Virtual<br>Gastric Band)</li>
      <li style="top:346px">Sugar Addiction</li>
      <li style="top:411px">Quit Smoking</li>
    </ul>
    <ul class="programs-list programs-list--right">
      <li style="top:225px">Chronic Fatigue &amp;<br>Chronic Pain Relief</li>
      <li style="top:335px">Stress Relief &amp; Deep<br>Relaxation</li>
    </ul>
  </section>

  <footer class="contact-band">
    <div class="contact-phone">
      <svg class="phone-icon" viewBox="0 0 100 100" aria-hidden="true">
        <circle cx="50" cy="50" r="45" fill="none" stroke="#ffffff" stroke-width="7"/>
        <path d="M35 24c3-2 6-1 7 2l4 10c1 2 0 5-2 6l-4 3c3 7 8 12 15 15l3-4c1-2 4-3 6-2l10 4c3 1 4 4 2 7l-4 6c-2 3-6 4-10 3-18-5-31-18-36-36-1-4 0-8 3-10z" fill="#ffffff"/>
      </svg>
      <span>1300 555 018</span>
    </div>
    <div class="contact-web">www.TranquilHarbourHypnotherapy.com.au</div>
  </footer>

</div>
</body>
</html>
```